Colin Petrie meat flyer

producer of specialist beef cuts. The beef are fed on a special diet of grain, red wine (3 litres each animal a day for 100 days) and apples and pears. 28 days hung. The various cuts of beef produced have a taste and texture never seen or tasted before.

See mock up of press release for wordings etc.

Target Market(s)

top class meat wholesalers and 5 star restaurants/hotels.

Industry/Entity Type

Graphic Design

Font styles to use
Script

Requirements
Must have
• the wine feeding regime is what gives the meat its very special taste and texture. referral to this is a must It is a unique way of feeding and is responsible for the texture.
• Australian black Angus is the breed of the cattle.
Nice to have
• it doesn't harm the animal in anyway due to the size of the beast.

```html
<!DOCTYPE html>
<html lang="en">
<head>
<meta charset="UTF-8">
<title>Verrick Luxury Meats – Wine Fed Beef &amp; Lambs</title>
<link href="https://fonts.googleapis.com/css2?family=Marcellus&family=Lato:wght@300;400;700&family=Great+Vibes&display=swap" rel="stylesheet">
<style>
  :root {
    --backdrop: #3b2a20;
    --paper: #cdbcab;
    --ink-dark: #5a3a2a;
    --ink-body: #7a6454;
    --photo-deep: #1f120b;
    --photo-mid: #5e331c;
    --photo-glow: #9a6236;
    --wine: #4a0f12;
    --cheese: #d8b872;
    --meat: #a3332c;
    --casing: #8a5a3a;
  }
  * { margin: 0; padding: 0; box-sizing: border-box; }
  html, body {
    width: 918px; height: 1200px; overflow: hidden;
    background: var(--backdrop);
  }
  .flyer {
    position: absolute; left: 130px; top: 135px;
    width: 658px; height: 930px;
    background: var(--paper);
    overflow: hidden;
  }
  .brand-name {
    position: absolute; top: 171px; left: 0; width: 100%;
    text-align: center;
    font-family: "Marcellus", serif;
    font-size: 19px; letter-spacing: 0.5px;
    color: var(--ink-dark);
  }
  .headline {
    position: absolute; top: 216px; left: 0; width: 100%;
    text-align: center;
    font-family: "Marcellus", serif; font-weight: 400;
    font-size: 38px; letter-spacing: 1.5px;
    color: var(--ink-dark);
  }
  .intro {
    position: absolute; top: 268px; left: 97px; width: 468px;
    font-family: "Lato", sans-serif; font-weight: 300;
    font-size: 13px; line-height: 18.6px;
    color: var(--ink-body);
    text-align: justify; text-align-last: center;
  }
  .intro p + p { margin-top: 9px; }
  .feature-photo {
    position: absolute; top: 483px; left: 0;
    width: 658px; height: 407px;
    background:
      radial-gradient(ellipse 16% 12% at 87% 60%, var(--meat) 0%, transparent 100%),
      radial-gradient(ellipse 17% 13% at 15% 58%, var(--meat) 0%, transparent 100%),
      radial-gradient(ellipse 14% 8% at 77% 57%, var(--cheese) 0%, transparent 100%),
      radial-gradient(ellipse 22% 12% at 23% 80%, var(--casing) 0%, transparent 100%),
      radial-gradient(ellipse 20% 14% at 88% 80%, var(--casing) 0%, transparent 100%),
      radial-gradient(ellipse 15% 10% at 30% 40%, var(--wine) 0%, transparent 100%),
      radial-gradient(ellipse 55% 45% at 55% 30%, var(--photo-glow) 0%, var(--photo-mid) 50%, transparent 85%),
      linear-gradient(180deg, var(--photo-deep) 0%, var(--photo-mid) 60%, #4a2414 100%);
  }
  .seal {
    position: absolute; left: 216px; top: 735px;
    width: 232px; height: 155px;
  }
  .seal-script {
    position: absolute; left: 216px; top: 836px; width: 232px;
    text-align: center;
    font-family: "Great Vibes", cursive;
    font-size: 31px; line-height: 36px; color: var(--ink-dark);
  }
</style>
</head>
<body>
  <article class="flyer">
    <div class="brand-name">VERRICK LUXURY MEATS</div>
    <h1 class="headline">WINE FED BEEF &amp; LAMBS</h1>
    <div class="intro">
      <p>Verrick Luxury Meats are producing ultra-premium wine fed Australian Black Angus Beef and Lamb for the export market. Our grapes are picked late with a high Baume count to increase sugar content, the wine is then blended into our livestock’s feeding regime along with quality orchard fruit.</p>
      <p>This with the formulated ration of GMO free, hormone free and Pasture Sure accredited grains and roughage. produces our unique product. Cattle are fed on our exclusive formula for up to 10 weeks. Depending on their weight they will consume up to 3 liters of wine per day. Lambs are also fed for up to 6 weeks with their wine ration increasing up to 500 mls per day.</p>
    </div>
    <div class="feature-photo" role="img" aria-label="Still life of two glasses of red wine, a glass decanter, a cheese knife in a wedge of hard cheese and sliced cured beef on a wooden board"></div>
    <svg class="seal" viewBox="0 0 232 155" role="img" aria-label="Wine and fruit fed seal">
      <path d="M0 155 V116 A116 116 0 0 1 232 116 V155 Z" fill="var(--paper)"/>
      <defs>
        <path id="seal-arc" d="M36 92 A82 82 0 0 1 196 92"/>
      </defs>
      <text font-family="Lato, sans-serif" font-weight="700" font-size="17" letter-spacing="1" fill="var(--ink-dark)">
        <textPath href="#seal-arc" startOffset="50%" text-anchor="middle">WINE &amp; FRUIT FED</textPath>
      </text>
    </svg>
    <div class="seal-script">Unique flavours</div>
  </article>
</body>
</html>
```